Flyer für Immobilienmakler
Top Arbeit vom Designer. Er hat alle Idee schnell und professionell umgesetzt und das Ergebnis kann sich sehen lassen. Herzlichen Dank für die großartige Arbeit. Immer wieder gerne.
Zielgruppe
Immobilienmakler, Zielgruppe sind Menschen die uns weiterempfehlen um ihre Immobilie zu verkaufen
Aufgabenstellung
Ein Flyer DIN lang quer, Vorder und Rückseite, Es geht um eine Tippgeberprovision welche Menschen bekommen die uns einen Verkaufskunden bringen, diese erhalten 10 %- genaue Texte und Hinweise werde ich einbringen, Unser Slogan: 'Unsere Erfahrung für Ihren Vorteil'
Nachtrag. Bei dem Flyer 'Haldrin Immobilien' finde ich die blauen Banner/ Streifen gut- ist aber kein Muss. Update: Es war als Inspiration von meiner Seite gedacht. Auf keinen Fall darf es genauso aussehen!!
Meine jetzige Webseite ist auch gut um die Farben zu erkennen, jedoch nicht unbedingt das Design, da ich gerade eine neue Webseite erstellen lasse

```html
<!DOCTYPE html>
<html lang="de">
<head>
<meta charset="utf-8">
<title>Aurelon Immobilien – Flyer DIN lang quer</title>
<link href="https://fonts.googleapis.com/css2?family=Poppins:wght@400;500;600;700;800&display=swap" rel="stylesheet">
<style>
  :root {
    --navy: #112a5c;
    --ink: #2b3065;
    --sand: #bba998;
    --white: #ffffff;
    --grey-bg: #999999;
    --text-grey: #555555;
  }
  * { box-sizing: border-box; margin: 0; padding: 0; }
  html, body { width: 1200px; height: 1117px; overflow: hidden; background: var(--grey-bg); font-family: "Poppins", sans-serif; }
  .flyer {
    position: absolute; left: 104px; width: 992px; height: 496px; overflow: hidden;
    background: var(--white); box-shadow: 0 8px 18px rgba(0,0,0,0.25);
  }
  .flyer--front { top: 48px; }
  .flyer--back { top: 572px; }
  .flyer__shapes { position: absolute; inset: 0; }
  .abs { position: absolute; }

  .brand { right: 64px; top: 58px; text-align: right; color: var(--ink); }
  .brand__name { font-size: 62px; font-weight: 600; letter-spacing: 4px; line-height: 1; display: block; }
  .brand__sub { font-size: 22px; font-weight: 400; color: #555; display: block; margin-top: 8px; }

  .slogan { left: 538px; top: 189px; width: 454px; height: 125px; background: var(--sand);
    color: var(--white); font-weight: 700; font-size: 41px; line-height: 52px;
    text-align: right; padding: 10px 46px 0 0; white-space: nowrap; }

  .intro { left: 55px; top: 344px; color: var(--white); font-weight: 700; font-size: 20.5px; line-height: 26px; white-space: nowrap; }

  .contact { left: 55px; top: 440px; width: 900px; height: 40px; display: flex; align-items: center; color: var(--white); font-size: 24px; white-space: nowrap; }
  .contact__item { display: flex; align-items: center; gap: 16px; flex: none; }
  .contact__item--web { font-weight: 700; }
  .contact__icon { width: 24px; height: 24px; flex: none; }
  .contact__divider { width: 2px; height: 36px; background: var(--white); margin: 0 22px; flex: none; }

  .offer__lead { left: 62px; top: 26px; font-size: 66px; font-weight: 700; color: var(--sand); line-height: 1; }
  .offer__figure { left: 58px; top: 88px; font-size: 152px; font-weight: 800; color: var(--ink); line-height: 1; letter-spacing: -4px; white-space: nowrap; }
  .offer__text { left: 63px; top: 226px; font-size: 18.5px; line-height: 21px; color: var(--text-grey); white-space: nowrap; }
  .offer__text strong { color: var(--navy); font-weight: 700; }

  .benefits { left: 55px; top: 367px; display: flex; }
  .benefit { display: flex; gap: 9px; width: 189px; color: var(--white); font-size: 10.5px; line-height: 15px; white-space: nowrap; }
  .benefit__tick { width: 13px; height: 13px; flex: none; margin-top: 1px; }
</style>
</head>
<body>

<section class="flyer flyer--front">
  <svg class="flyer__shapes" viewBox="0 0 992 496">
    <defs>
      <linearGradient id="houseTone" x1="0" y1="0" x2="1" y2="1">
        <stop offset="0" stop-color="#b9c2d8"/>
        <stop offset="0.45" stop-color="#e3e1df"/>
        <stop offset="1" stop-color="#b59e86"/>
      </linearGradient>
      <linearGradient id="skyFade" x1="0" y1="0" x2="1" y2="0">
        <stop offset="0.45" stop-color="#ffffff" stop-opacity="0"/>
        <stop offset="0.75" stop-color="#ffffff" stop-opacity="0.92"/>
      </linearGradient>
    </defs>
    <rect width="992" height="496" fill="url(#houseTone)" role="img" aria-label="Foto: moderne weiße Reihenhäuser mit Holzelementen, Gärten und Bäumen"/>
    <rect width="992" height="200" fill="url(#skyFade)"/>
    <path d="M0 344 C120 290 260 298 420 352 C560 400 640 430 730 418 C860 402 940 385 992 362 L992 496 L0 496 Z" fill="var(--sand)"/>
    <path d="M0 352 C120 300 260 308 420 362 C560 410 640 420 730 410 C860 394 940 378 992 372 L992 496 L0 496 Z" fill="var(--navy)"/>
  </svg>

  <div class="abs brand">
    <span class="brand__name">AURELON</span>
    <span class="brand__sub">Immobilien</span>
  </div>

  <div class="abs slogan">Unsere Erfahrung<br>für Ihren Vorteil</div>

  <p class="abs intro">Wir unterstützen Sie im<br>gesamten Prozess mit unserem<br>einzigartigen Modulsystem.</p>

  <div class="abs contact">
    <span class="contact__item">
      <svg class="contact__icon" viewBox="0 0 24 24"><circle cx="12" cy="12" r="12" fill="var(--sand)"/><path d="M8 6 L10 6 L11 9 L9.5 10.5 C10.3 12.2 11.8 13.7 13.5 14.5 L15 13 L18 14 L18 16 C18 17 17 18 16 18 C10.5 18 6 13.5 6 8 C6 7 7 6 8 6 Z" fill="var(--navy)"/></svg>
      +49 (0)6251 4471902
    </span>
    <span class="contact__divider"></span>
    <span class="contact__item">
      <svg class="contact__icon" viewBox="0 0 24 24"><circle cx="12" cy="12" r="12" fill="var(--sand)"/><rect x="6" y="8" width="12" height="8.5" fill="none" stroke="var(--navy)" stroke-width="1.4"/><path d="M6 8 L12 13 L18 8" fill="none" stroke="var(--navy)" stroke-width="1.4"/></svg>
      kontakt@aurelon.immo
    </span>
    <span class="contact__divider"></span>
    <span class="contact__item contact__item--web">
      <svg class="contact__icon" viewBox="0 0 24 24"><circle cx="12" cy="12" r="12" fill="var(--sand)"/><g fill="none" stroke="var(--navy)" stroke-width="1.3"><circle cx="12" cy="12" r="6.5"/><ellipse cx="12" cy="12" rx="3" ry="6.5"/><path d="M5.5 12 H18.5 M6.5 9 H17.5 M6.5 15 H17.5"/></g></svg>
      aurelon.immo
    </span>
  </div>
</section>

<section class="flyer flyer--back">
  <svg class="flyer__shapes" viewBox="0 0 992 496">
    <defs>
      <linearGradient id="kitchenTone" x1="0" y1="0" x2="0" y2="1">
        <stop offset="0" stop-color="#ecebe8"/>
        <stop offset="0.5" stop-color="#d9d3cb"/>
        <stop offset="0.75" stop-color="#b27a45"/>
        <stop offset="1" stop-color="#c4b29c"/>
      </linearGradient>
    </defs>
    <polygon points="516,0 992,0 992,496 420,496" fill="url(#kitchenTone)" role="img" aria-label="Foto: helle Küche mit Holzfronten, Einbaubackofen, Fenster mit Jalousien und Pflanzen"/>
    <polygon points="502,0 516,0 452,357 439,357" fill="var(--ink)"/>
    <path d="M0 349 C130 290 280 300 440 360 C560 405 620 425 700 420 C830 410 930 385 992 366 L992 496 L0 496 Z" fill="var(--sand)"/>
    <path d="M0 358 C130 300 280 310 440 370 C560 415 620 414 700 412 C830 404 930 380 992 376 L992 496 L0 496 Z" fill="var(--navy)"/>
  </svg>

  <div class="abs offer__lead">Erhalten</div>
  <div class="abs offer__figure">10%-</div>
  <p class="abs offer__text">indem Sie es den Menschen empfehlen,<br>die Ihnen am nächsten stehen<br><strong>ihr Eigentum an uns zu verkaufen</strong></p>

  <div class="abs benefits">
    <div class="benefit">
      <svg class="benefit__tick" viewBox="0 0 14 14"><circle cx="7" cy="7" r="7" fill="var(--sand)"/><path d="M4 7.2 L6.2 9.3 L10 5" fill="none" stroke="var(--navy)" stroke-width="1.6"/></svg>
      <span>Lorem ipsum dolor sit amet,<br>consectetur adipiscing<br>elit sed do eiusmod tempor<br>incididunt ut labore</span>
    </div>
    <div class="benefit">
      <svg class="benefit__tick" viewBox="0 0 14 14"><circle cx="7" cy="7" r="7" fill="var(--sand)"/><path d="M4 7.2 L6.2 9.3 L10 5" fill="none" stroke="var(--navy)" stroke-width="1.6"/></svg>
      <span>Lorem ipsum dolor sit amet,<br>consectetur adipiscing<br>elit sed do eiusmod tempor<br>incididunt ut labore</span>
    </div>
  </div>

  <div class="abs contact">
    <span class="contact__item">
      <svg class="contact__icon" viewBox="0 0 24 24"><circle cx="12" cy="12" r="12" fill="var(--sand)"/><path d="M8 6 L10 6 L11 9 L9.5 10.5 C10.3 12.2 11.8 13.7 13.5 14.5 L15 13 L18 14 L18 16 C18 17 17 18 16 18 C10.5 18 6 13.5 6 8 C6 7 7 6 8 6 Z" fill="var(--navy)"/></svg>
      +49 (0)6251 4471902
    </span>
    <span class="contact__divider"></span>
    <span class="contact__item">
      <svg class="contact__icon" viewBox="0 0 24 24"><circle cx="12" cy="12" r="12" fill="var(--sand)"/><rect x="6" y="8" width="12" height="8.5" fill="none" stroke="var(--navy)" stroke-width="1.4"/><path d="M6 8 L12 13 L18 8" fill="none" stroke="var(--navy)" stroke-width="1.4"/></svg>
      kontakt@aurelon.immo
    </span>
    <span class="contact__divider"></span>
    <span class="contact__item contact__item--web">
      <svg class="contact__icon" viewBox="0 0 24 24"><circle cx="12" cy="12" r="12" fill="var(--sand)"/><g fill="none" stroke="var(--navy)" stroke-width="1.3"><circle cx="12" cy="12" r="6.5"/><ellipse cx="12" cy="12" rx="3" ry="6.5"/><path d="M5.5 12 H18.5 M6.5 9 H17.5 M6.5 15 H17.5"/></g></svg>
      aurelon.immo
    </span>
  </div>
</section>

</body>
</html>
```